Crash repair flyer design

We need a basic flyer to distribute to potential clients and insurance companies. The design should be professional looking, uncluttered and to the point. Title should be 'Bright Lane Body Repairs' and be in a dark blue font. It should have a few pictures, some facts and a brief description of the business. Information can be taken from our website 'brightlanebodyrepairs.example.au'

Target Market(s)

insurance companies and general

Industry/Entity Type

Insurance

Requirements
Must have
• Company Logo
"for all your crash repair needs" to be placed somewhere.
'KGM Approved'
PLW Approved'
'CORVO SA Approved'
Nice to have
• picture of the front of the building.
picture of car being painted in the spraybooth
Should not have
• Not too may colors

```html
<!DOCTYPE html>
<html lang="en">
<head>
<meta charset="utf-8">
<title>Bright Lane Body Repairs – Flyer</title>
<link href="https://fonts.googleapis.com/css2?family=Anton&family=Oswald:wght@500;700&family=Arimo:wght@400;700&display=swap" rel="stylesheet">
<style>
:root{
  --navy:#0f1466;
  --blue:#1f5fb0;
  --light-blue:#a9c0ea;
  --sky:#8fa9dc;
  --red:#b52f38;
  --yellow:#ffe400;
  --white:#ffffff;
  --ink:#111111;
}
*{box-sizing:border-box;margin:0;padding:0}
html,body{width:1200px;height:763px;overflow:hidden;background:var(--white)}
body{position:relative;font-family:"Arimo",Arial,sans-serif}
.sheet-label{position:absolute;top:12px;font:700 9px "Arimo",Arial,sans-serif;color:var(--ink);width:514px;text-align:center}
.sheet-label--back{left:69px}
.sheet-label--front{left:623px}
.page{position:absolute;top:35px;width:514px;height:688px;overflow:hidden;
  background:linear-gradient(160deg,#9cb3e2 0%,#86a1d6 45%,#a4baea 100%)}
.page--back{left:69px}
.page--front{left:623px}
.page-shapes{position:absolute;inset:0;width:100%;height:100%}
.brand{position:absolute;display:flex;align-items:center;gap:10px}
.brand-dot{width:30px;height:30px;border-radius:50%;background:var(--red)}
.brand-name{font:700 18px "Arimo",Arial,sans-serif;color:var(--navy);letter-spacing:.3px;text-transform:uppercase}
.back-brand{left:57px;top:30px}
.photo{position:absolute;background:linear-gradient(180deg,#b8bcc2 0%,#8f959c 55%,#6d7278 100%)}
.photo-tag{position:absolute;right:6px;bottom:2px;font:500 15px "Oswald",sans-serif;color:var(--white);letter-spacing:.5px}
.photo--before{left:57px;top:94px;width:164px;height:122px}
.photo--after{left:246px;top:94px;width:164px;height:122px}
.about{position:absolute;left:65px;top:229px;width:436px;font-size:9.6px;line-height:11.8px;color:var(--navy)}
.about p+p{margin-top:11.8px}
.services-title{position:absolute;left:169px;top:383px;width:212px;height:22px;border-radius:10px 10px 0 0;background:var(--navy);
  color:var(--white);font:700 11px "Arimo",Arial,sans-serif;text-align:center;line-height:22px}
.services{position:absolute;left:67px;top:405px;width:410px;height:139px;background:var(--red);
  display:grid;grid-template-columns:234px 1fr;padding:9px 0 0 14px}
.services ul{list-style:none}
.services li{font:700 10px "Arimo",Arial,sans-serif;color:var(--white);line-height:17.6px}
.contact{position:absolute;left:113px;top:551px;font-size:9.6px;line-height:12px;color:var(--ink);font-weight:700}
.contact-name{color:var(--red);margin:10px 0 10px}
.contact dl{display:grid;grid-template-columns:auto 1fr;column-gap:6px}
.front-brand{position:absolute;left:230px;top:16px;width:270px;text-align:center}
.front-brand .brand-dot{width:58px;height:58px;margin:0 auto 8px}
.front-brand .brand-name{font-size:15px}
.headline{position:absolute;left:132px;top:74px;transform:rotate(13.4deg);transform-origin:left top;
  font:400 37px "Anton",sans-serif;color:var(--navy);white-space:nowrap;letter-spacing:-.3px}
.tagline{position:absolute;left:160px;top:505px;transform:rotate(-26.5deg);transform-origin:left top;
  font:500 28px "Oswald",sans-serif;color:var(--white);white-space:nowrap}
.perks{position:absolute;left:300px;top:455px;width:175px;height:178px}
.perk-house{position:absolute;left:0;top:0;width:175px;height:178px}
.perk-list{position:absolute;left:18px;top:92px;list-style:none}
.perk-list li{display:flex;align-items:center;gap:5px;font:700 8.4px "Arimo",Arial,sans-serif;color:var(--navy);line-height:14.7px;white-space:nowrap}
.tick{display:block;width:10px;height:10px;flex:none}
.badge{position:absolute}
.badge--plw{left:71px;top:627px;width:50px;height:52px;background:var(--blue)}
.badge--kgm{left:136px;top:624px;width:44px;height:56px;background:var(--white);padding:3px}
.badge--kgm span{display:block;width:100%;height:100%;background:var(--yellow)}
.fleet-note{position:absolute;left:197px;top:638px;width:270px;height:31px;background:var(--blue);
  display:flex;align-items:center;padding:0 6px 0 8px;gap:8px}
.fleet-note p{font-size:7px;line-height:8.6px;color:var(--white);text-align:center;flex:1}
.fleet-note span{width:46px;height:20px;border-radius:10px;background:var(--white);flex:none}
</style>
</head>
<body>

<div class="sheet-label sheet-label--back">FLYER DESIGN BACK</div>
<div class="sheet-label sheet-label--front">FLYER DESIGN FRONT</div>

<section class="page page--back">
  <svg class="page-shapes" viewBox="0 0 514 688" preserveAspectRatio="none" aria-hidden="true">
    <polygon points="3,92 514,92 514,662 3,662" fill="#ffffff"/>
    <polygon points="360,140 514,74 514,88 380,140" fill="#1f5fb0"/>
    <polygon points="390,140 514,88 514,102 420,140" fill="#a9c0ea"/>
    <polygon points="430,140 514,104 514,112 450,140" fill="#0f1466"/>
    <polygon points="0,290 62,258 62,268 0,302" fill="#1f5fb0"/>
    <polygon points="0,304 62,272 62,282 0,316" fill="#a9c0ea"/>
    <polygon points="372,662 514,500 514,662" fill="#0f1466"/>
    <polygon points="455,662 514,592 514,662" fill="#1f5fb0"/>
  </svg>

  <div class="brand back-brand">
    <span class="brand-dot"></span>
    <span class="brand-name">Bright Lane Body Repairs</span>
  </div>

  <div class="photo photo--before" role="img" aria-label="Photo of a silver sedan front before repair"><span class="photo-tag">BEFORE</span></div>
  <div class="photo photo--after" role="img" aria-label="Photo of the same silver sedan front after repair"><span class="photo-tag">AFTER</span></div>

  <div class="about">
    <p>BLB Repairs are a full service Crash Repair and Paint refinishing specialist center located in the Kenfield/Bay Park area, and within<br>10 km's of the CBD. BLB Repairs has been operating for over 31 years and have repaired over 20,000 vehicles under the same ownership and has 11 professional staff members including trained technicians, estimators and office support personnel.</p>
    <p>We believe that it is our attention to detail that gives us the edge over our competitors. We have implemented a quality system that ensures that all work carried out is checked and meets the relevant standards. Ensuring that your vehicle is returned to its pre-accident state. Our specialised repair equipment and new technology enables us to correctly repair domestic and imported vehicles.</p>
  </div>

  <div class="services-title">We specialize in the following</div>
  <div class="services">
    <ul>
      <li>&gt; Quality Assured System</li>
      <li>&gt; Private &amp; Insurance Work</li>
      <li>&gt; Spray Painting &amp; Panel Beating</li>
      <li>&gt; Chassis Straightening &amp; Measuring System</li>
      <li>&gt; All Makes &amp; Models</li>
      <li>&gt; Expert Colour Matching</li>
      <li>&gt; Detailing</li>
    </ul>
    <ul>
      <li>&gt; 2 Pac Technology</li>
      <li>&gt; Spray Booth Oven</li>
      <li>&gt; Replacement Windscreens</li>
      <li>&gt; Re-Gas Air Conditioning</li>
      <li>&gt; Claim Form Service</li>
      <li>&gt; Pre-Sale Polish &amp; Touch Ups</li>
      <li>&gt; Custom Paint Work</li>
    </ul>
  </div>

  <div class="contact">
    <p>Contact Details:</p>
    <p class="contact-name">Daniel or Mark Keravos</p>
    <dl>
      <dt>Address:</dt><dd>42 Harlow Road, Kenfield, S.A. 5090</dd>
      <dt>Phone No:</dt><dd>(08) 5550 1234</dd>
      <dt>Fax:</dt><dd>(08) 5550 1235</dd>
      <dt>Email:</dt><dd>admin@brightlanebodyrepairs.example.au</dd>
    </dl>
  </div>
</section>

<section class="page page--front">
  <svg class="page-shapes" viewBox="0 0 514 688" preserveAspectRatio="none" aria-hidden="true">
    <polygon points="130,120 514,212 514,228 128,134" fill="#1f5fb0"/>
    <polygon points="128,134 514,228 514,240 126,146" fill="#a9c0ea"/>
    <polygon points="0,122 514,240 514,355 0,512" fill="#9aa0a6"/>
    <polygon points="110,600 129,518 514,324 514,398" fill="#0f1466"/>
    <polygon points="105,612 514,405 514,420 100,630" fill="#1f5fb0"/>
  </svg>
  <div class="photo" role="img" aria-label="Photo of a masked silver car being painted in the spray booth"
       style="left:0;top:0;width:514px;height:688px;clip-path:polygon(0 122px,514px 240px,514px 340px,120px 520px,0 512px);background:linear-gradient(170deg,#d9dadc 0%,#b7b9bc 45%,#7e8287 100%)"></div>

  <div class="front-brand">
    <div class="brand-dot"></div>
    <div class="brand-name">Bright Lane Body Repairs</div>
  </div>

  <div class="headline">Bright Lane Body Repairs</div>
  <div class="tagline">For all your crash repair needs</div>

  <div class="perks">
    <svg class="perk-house" viewBox="0 0 175 178" aria-hidden="true">
      <polygon points="87,0 175,90 166,90 166,178 8,178 8,90 0,90" fill="#ffe400"/>
      <g transform="translate(70,45) rotate(-25)">
        <rect x="0" y="6" width="40" height="8" rx="3" fill="#111"/>
        <circle cx="42" cy="10" r="9" fill="#111"/>
        <rect x="42" y="6" width="12" height="8" fill="#ffe400"/>
      </g>
    </svg>
    <ul class="perk-list">
      <li><svg class="tick" viewBox="0 0 10 10" aria-hidden="true"><circle cx="5" cy="5" r="5" fill="#0f1466"/><path d="M2.6 5.2l1.6 1.6 3.2-3.4" stroke="#fff" stroke-width="1.3" fill="none"/></svg>Friendly And Experienced Staff</li>
      <li><svg class="tick" viewBox="0 0 10 10" aria-hidden="true"><circle cx="5" cy="5" r="5" fill="#0f1466"/><path d="M2.6 5.2l1.6 1.6 3.2-3.4" stroke="#fff" stroke-width="1.3" fill="none"/></svg>Recommended Repairer</li>
      <li><svg class="tick" viewBox="0 0 10 10" aria-hidden="true"><circle cx="5" cy="5" r="5" fill="#0f1466"/><path d="M2.6 5.2l1.6 1.6 3.2-3.4" stroke="#fff" stroke-width="1.3" fill="none"/></svg>No Appointment Necessary</li>
      <li><svg class="tick" viewBox="0 0 10 10" aria-hidden="true"><circle cx="5" cy="5" r="5" fill="#0f1466"/><path d="M2.6 5.2l1.6 1.6 3.2-3.4" stroke="#fff" stroke-width="1.3" fill="none"/></svg>Modern Loan Cars Available</li>
      <li><svg class="tick" viewBox="0 0 10 10" aria-hidden="true"><circle cx="5" cy="5" r="5" fill="#0f1466"/><path d="M2.6 5.2l1.6 1.6 3.2-3.4" stroke="#fff" stroke-width="1.3" fill="none"/></svg>Free Quotes</li>
    </ul>
  </div>

  <div class="badge badge--plw" role="img" aria-label="PLW approved badge"></div>
  <div class="badge badge--kgm" role="img" aria-label="KGM approved repairer badge"><span></span></div>
  <div class="fleet-note">
    <p>CORVO SA is the trading name of the Fleet Division of the Southern Regional Government Finance Office</p>
    <span role="img" aria-label="CORVO SA approved badge"></span>
  </div>
</section>

</body>
</html>
```